the orbit dental works
Cards,Letterheads, Sticker, etc
Modern
Milton Crawshay
Suite 4, 61 Holloway Street
Bellmore NSW 2287
theorbitdental@fernmail.com.au
theorbitdental.com.au
Second Name; Judith Crawshay.
We also need a sticker to place on packaging to promote business

```html
<!DOCTYPE html>
<html lang="en">
<head>
<meta charset="utf-8">
<title>the orbit dental works – business card</title>
<link rel="stylesheet" href="https://fonts.googleapis.com/css2?family=Arimo:wght@400;700&family=Dancing+Script:wght@500&display=swap">
<style>
  :root {
    --page-bg: #ffffff;
    --frame: #8a8a8a;
    --card-edge: #9a9a9a;
    --front-light: #ffffff;
    --front-mid: #e4e4e4;
    --front-dark: #c9c9c9;
    --ink: #111111;
    --blue-deep: #0d3f9c;
    --blue-mid: #1f6fd0;
    --blue-bright: #3a9cf0;
    --blue-glow: #7cc4f7;
    --brand-blue: #2f6fc4;
    --white: #ffffff;
  }
  * { margin: 0; padding: 0; box-sizing: border-box; }
  html, body { width: 1200px; height: 802px; overflow: hidden; background: var(--page-bg); }
  .canvas {
    position: relative; width: 1200px; height: 802px;
    border: 2px solid var(--frame); background: var(--page-bg);
    font-family: "Arimo", Arial, sans-serif;
  }
  .card {
    position: absolute; top: 137px; width: 318px; height: 530px;
    border: 1px solid var(--card-edge); overflow: hidden;
  }
  .card--front {
    left: 247px;
    background: linear-gradient(180deg, var(--front-light) 0%, var(--front-mid) 30%, var(--front-light) 55%, var(--front-dark) 100%);
  }
  .card--back {
    left: 612px;
    background: radial-gradient(circle at 50% 42%, var(--blue-bright) 0%, var(--blue-mid) 38%, var(--blue-deep) 100%);
  }
  .brand {
    position: absolute; left: 32px; top: 28px;
    display: flex; align-items: center; gap: 9px;
    color: var(--brand-blue); font-weight: 700; font-size: 18px; white-space: nowrap;
  }
  .brand__dot {
    width: 32px; height: 32px; border-radius: 50%;
    background: var(--brand-blue);
  }
  .holder-name {
    position: absolute; left: 0; right: 0; top: 208px;
    text-align: center; font-weight: 700; font-size: 24px; color: var(--ink);
  }
  .contact {
    position: absolute; left: 0; right: 0; top: 380px;
    text-align: center; font-size: 9.5px; line-height: 17px; color: var(--ink);
  }
  .wave { position: absolute; left: 0; bottom: 0; width: 318px; height: 92px; }
  .corner-mark {
    position: absolute; left: 250px; top: 465px;
    width: 48px; height: 48px; border-radius: 50%;
    background: rgba(255,255,255,0.35);
  }
  .emblem {
    position: absolute; left: 50%; top: 128px; transform: translateX(-50%);
    display: flex; flex-direction: column; align-items: center; gap: 14px;
  }
  .emblem__circle {
    width: 170px; height: 170px; border-radius: 50%;
    background: radial-gradient(circle at 50% 40%, rgba(255,255,255,0.55), rgba(124,196,247,0.25) 70%, rgba(124,196,247,0));
  }
  .emblem__name { color: var(--white); font-weight: 700; font-size: 15px; white-space: nowrap; }
  .tagline {
    position: absolute; left: 40px; top: 478px;
    font-family: "Dancing Script", cursive; font-size: 20px; color: var(--white);
  }
</style>
</head>
<body>
<div class="canvas">
  <section class="card card--front">
    <div class="brand"><span class="brand__dot"></span><span class="brand__name">the orbit dental works</span></div>
    <h1 class="holder-name">Milton Crawshay</h1>
    <p class="contact">
      Suite 4, 61 Holloway Street Bellmore NSW 2287<br>
      Phone: 02 4955 0173 Email: theorbitdental@fernmail.com.au<br>
      www.theorbitdental.com.au
    </p>
    <svg class="wave" viewBox="0 0 318 92" preserveAspectRatio="none" aria-hidden="true">
      <defs>
        <linearGradient id="waveFill" x1="0" y1="0" x2="1" y2="1">
          <stop offset="0" stop-color="#3a9cf0"/>
          <stop offset="0.6" stop-color="#1f6fd0"/>
          <stop offset="1" stop-color="#0d3f9c"/>
        </linearGradient>
      </defs>
      <path d="M0 16 C85 44 185 48 318 8 L318 92 L0 92 Z" fill="url(#waveFill)"/>
      <path d="M0 9 C85 37 185 41 318 1" fill="none" stroke="#1f6fd0" stroke-width="2"/>
    </svg>
    <span class="corner-mark"></span>
  </section>

  <section class="card card--back">
    <div class="emblem">
      <span class="emblem__circle"></span>
      <span class="emblem__name">the orbit dental works</span>
    </div>
    <p class="tagline">smiles made to last</p>
  </section>
</div>
</body>
</html>
```